KVT Stationery
KVT - Bright Channel Partners - Media Representatives
Project: KVT Stationery
KVT Stationery - News and Media
Creative Brief
Use same font as used in my logo
Omar Haddine
Regional Sales Director
Sahil Road - Harat El Nour St. Al Jabiya Al Saffa 3 Building - 7th Floor - Office 703-704
o.haddine@kvtgroupco.co
www.kvtgroupco.co
Logos of the media they represent: Lazeezo Oru etc... NB: you will find them here attached

```html
<!DOCTYPE html>
<html lang="en">
<head>
<meta charset="utf-8">
<title>KVT Stationery – Business Card</title>
<link href="https://fonts.googleapis.com/css2?family=Roboto:wght@400;700;900&family=Roboto+Condensed:wght@400;700&display=swap" rel="stylesheet">
<style>
  :root{
    --bg:#d9d6d2;
    --card:#ffffff;
    --grey-dark:#5e5e5e;
    --grey-mid:#8a8a8a;
    --grey-light:#c9c9c9;
    --orange:#f39200;
    --orange-light:#f7b541;
    --ink:#3a3a3a;
    --white:#ffffff;
  }
  *{box-sizing:border-box;margin:0;padding:0}
  html,body{width:1200px;height:751px;overflow:hidden;background:var(--bg)}
  body{position:relative;font-family:"Roboto",Arial,sans-serif;color:var(--ink)}

  .card{position:absolute;top:225px;width:520px;height:300px;background:var(--card);
        border-radius:14px;overflow:hidden;box-shadow:0 6px 18px rgba(0,0,0,.18)}
  .card--front{left:50px}
  .card--back{left:630px}

  .card__wave{position:absolute;inset:0;width:100%;height:100%}

  .brand{position:absolute;display:flex;flex-direction:column}
  .brand__mark{display:flex;align-items:center;gap:8px;font-family:"Roboto Condensed",sans-serif;
               font-weight:700;color:var(--grey-mid);letter-spacing:1px;line-height:1}
  .brand__dot{border-radius:50%;background:var(--orange)}
  .brand__name{font-family:"Roboto",sans-serif;font-weight:900;color:var(--ink);letter-spacing:-.3px}
  .brand__tag{font-family:"Roboto Condensed",sans-serif;color:var(--grey-mid);letter-spacing:3px;
              border-top:1px solid var(--grey-light);text-align:center}

  .card--front .brand{left:34px;top:30px}
  .card--front .brand__mark{font-size:46px}
  .card--front .brand__dot{width:16px;height:16px}
  .card--front .brand__name{font-size:16px;margin-top:4px}
  .card--front .brand__tag{font-size:10px;padding-top:2px}

  .person{position:absolute;left:40px;top:140px}
  .person__name{color:var(--orange);font-weight:700;font-size:17px}
  .person__role{color:var(--grey-mid);font-size:9px;margin-top:2px}

  .contact{position:absolute;left:322px;top:158px;width:186px;color:var(--white);
           font-family:"Roboto Condensed",sans-serif;font-size:9.5px;line-height:13px}
  .contact__address{margin-bottom:6px}
  .contact__row{display:flex;align-items:center;gap:6px}
  .contact__icon{width:9px;height:9px;flex:none}

  .card--back .brand{left:0;right:0;top:40px;align-items:center}
  .card--back .brand__mark{font-size:50px}
  .card--back .brand__dot{width:18px;height:18px}
  .card--back .brand__name{font-size:18px;margin-top:4px}
  .card--back .brand__tag{font-size:11px;padding-top:2px;width:230px}

  .channels{position:absolute;left:22px;right:22px;top:180px;display:flex;
            justify-content:space-between;align-items:center}
  .channel{display:flex;flex-direction:column;align-items:center;gap:6px}
  .channel__shape{width:44px;height:44px;border-radius:50%}
  .channel__shape--square{border-radius:4px}
  .channel__name{font-size:10px;font-weight:700;color:var(--ink)}

  .card__strip{position:absolute;left:0;right:0;bottom:0;height:14px;
               background:linear-gradient(90deg,var(--orange),var(--orange-light) 60%,var(--grey-light))}
</style>
</head>
<body>

<section class="card card--front">
  <svg class="card__wave" viewBox="0 0 520 300" preserveAspectRatio="none" aria-hidden="true">
    <defs>
      <linearGradient id="greyFill" x1="0" y1="0" x2="0" y2="1">
        <stop offset="0" stop-color="#7a7a7a"/>
        <stop offset="1" stop-color="#4f4f4f"/>
      </linearGradient>
    </defs>
    <path d="M0,300 L0,245 C140,255 230,205 300,145 C360,95 440,75 520,75 L520,300 Z" fill="url(#greyFill)"/>
    <path d="M0,237 C140,247 230,197 300,137 C360,87 440,67 520,67" fill="none" stroke="#f39200" stroke-width="8"/>
    <path d="M0,227 C140,237 230,187 300,127 C360,77 440,57 520,57" fill="none" stroke="#c9c9c9" stroke-width="5"/>
    <path d="M0,219 C140,229 230,179 300,119 C360,69 440,49 520,49" fill="none" stroke="#f7b541" stroke-width="2"/>
  </svg>

  <div class="brand">
    <div class="brand__mark"><span class="brand__dot"></span>KVT</div>
    <div class="brand__name">Bright Channel Partners</div>
    <div class="brand__tag">Media Representatives</div>
  </div>

  <div class="person">
    <div class="person__name">Omar Haddine</div>
    <div class="person__role">Regional Sales Director</div>
  </div>

  <div class="contact">
    <p class="contact__address">Sahil Road - Harat El Nour St. Al Jabiya Al Saffa 3 Building - 7th Floor - Office 703-704</p>
    <p class="contact__row"><svg class="contact__icon" viewBox="0 0 10 10"><path d="M2,1 L4,1 L4.5,3 L3.3,4 C4,5.5 4.5,6 6,6.7 L7,5.5 L9,6 L9,8 C5,8.5 1.5,5 2,1 Z" fill="#fff"/></svg>+000 2 555 0143</p>
    <p class="contact__row"><svg class="contact__icon" viewBox="0 0 10 10"><rect x="2.5" y="0.5" width="5" height="9" rx="1" fill="#fff"/></svg>+000 55 555 0182</p>
    <p class="contact__row"><svg class="contact__icon" viewBox="0 0 10 10"><rect x="1" y="3" width="8" height="5" fill="#fff"/><rect x="3" y="1" width="4" height="2" fill="#fff"/></svg>+000 2 555 0167</p>
    <p class="contact__row"><svg class="contact__icon" viewBox="0 0 10 10"><rect x="0.5" y="2" width="9" height="6" fill="#fff"/><path d="M0.5,2 L5,5.5 L9.5,2" fill="none" stroke="#5e5e5e" stroke-width="1"/></svg>o.haddine@kvtgroupco.co</p>
    <p class="contact__row"><svg class="contact__icon" viewBox="0 0 10 10"><circle cx="5" cy="5" r="4.3" fill="none" stroke="#fff" stroke-width="1.2"/><path d="M1,5 H9 M5,1 V9" stroke="#fff" stroke-width="0.8"/></svg>www.kvtgroupco.co</p>
  </div>
</section>

<section class="card card--back">
  <div class="brand">
    <div class="brand__mark"><span class="brand__dot"></span>KVT</div>
    <div class="brand__name">Bright Channel Partners</div>
    <div class="brand__tag">Media Representatives</div>
  </div>

  <div class="channels">
    <div class="channel"><span class="channel__shape channel__shape--square" style="background:#d7192a"></span><span class="channel__name">Matchday</span></div>
    <div class="channel"><span class="channel__shape" style="background:#e7b416"></span><span class="channel__name">Lazeezo</span></div>
    <div class="channel"><span class="channel__shape" style="background:#2f5fb3"></span><span class="channel__name">Oru TV</span></div>
    <div class="channel"><span class="channel__shape" style="background:#3a4fa8"></span><span class="channel__name">Oru Aflam</span></div>
    <div class="channel"><span class="channel__shape" style="background:#2a9fd8"></span><span class="channel__name">Visiona</span></div>
    <div class="channel"><span class="channel__shape" style="background:#5bb13c"></span><span class="channel__name">Pebble Kids</span></div>
  </div>

  <div class="card__strip"></div>
</section>

</body>
</html>
```